Offshore Energy Projects Management Consultancy needs a business card design

Logo available. We provide teams to deliver engineering consultancy, project management and delivery teams mainly in the offshore renewables sector. The company is all about bringing the right people to a project to deliver the scope.

The business card will be used for all staff.

The business card should be quite simple, vibrant and uncluttered but convey experience, enthusiasm and integration.

Target Market(s)

Energy Project Developers and Tier 1 construction companies

Contact Information for Business Card

Logo should be on the back of the card. I'm happy for the designer to play with the colour of the logo and background colour.

Front of the card should convey all the must have information in a clear and professional manner but without being overly traditional.

Colors

Designer to choose colors to be used in the design.

Requirements
Must have
• Land Line Tel Number, Mobile Tel Number, Email, business address, web address.

```html
<!DOCTYPE html>
<html lang="en">
<head>
<meta charset="utf-8">
<title>Northwind Delivery Group – Business Card</title>
<link rel="stylesheet" href="https://fonts.googleapis.com/css2?family=Open+Sans:wght@400;600;700&display=swap">
<style>
  :root {
    --bg: #c9cbce;
    --blue: #1074bf;
    --blue-light: #27a3dc;
    --blue-dark: #0f69ad;
    --ink: #5a5d61;
    --name: #1a6fb8;
    --white: #ffffff;
    --paper: #f4f5f6;
  }
  * { box-sizing: border-box; margin: 0; padding: 0; }
  html, body { width: 1200px; height: 800px; overflow: hidden; }
  body {
    background: var(--bg);
    font-family: "Open Sans", Arial, sans-serif;
    position: relative;
  }
  .card {
    position: absolute;
    left: 320px;
    width: 560px;
    height: 320px;
    box-shadow: 0 6px 16px rgba(0,0,0,0.25);
    overflow: hidden;
  }
  /* Back */
  .card-back {
    top: 50px;
    background: var(--blue);
    color: var(--white);
    display: flex;
    flex-direction: column;
    align-items: center;
  }
  .card-back .brand {
    margin-top: 118px;
    display: flex;
    align-items: center;
    gap: 12px;
    font-size: 26px;
    font-weight: 600;
    letter-spacing: 0.5px;
    color: var(--white);
  }
  .brand-dot {
    width: 18px; height: 18px;
    border-radius: 50%;
    background: var(--white);
    flex: none;
  }
  .card-back .web {
    margin-top: 72px;
    font-size: 15px;
    letter-spacing: 2.5px;
  }
  /* Front */
  .card-front {
    top: 420px;
    background: linear-gradient(180deg, var(--white) 0%, var(--paper) 100%);
  }
  .card-front .wave { position: absolute; left: 0; top: 0; }
  .card-front .brand {
    position: absolute;
    left: 34px;
    top: 100px;
    width: 230px;
    display: flex;
    align-items: center;
    gap: 10px;
    font-size: 19px;
    font-weight: 600;
    line-height: 1.2;
    color: var(--blue);
  }
  .card-front .brand .brand-dot { background: var(--blue); width: 14px; height: 14px; }
  .divider {
    position: absolute;
    left: 290px;
    top: 50px;
    width: 1.5px;
    height: 140px;
    background: linear-gradient(180deg, var(--blue-light) 0%, var(--blue-light) 30%, var(--ink) 30%, var(--ink) 100%);
  }
  .contact {
    position: absolute;
    left: 318px;
    top: 52px;
  }
  .person-name {
    font-size: 20px;
    font-weight: 700;
    color: var(--name);
  }
  .person-role {
    font-size: 14px;
    color: var(--blue-light);
    margin-bottom: 12px;
  }
  .contact-list { list-style: none; }
  .contact-list li {
    display: flex;
    align-items: center;
    gap: 8px;
    font-size: 14px;
    color: var(--ink);
    line-height: 19px;
  }
  .contact-list svg { width: 13px; height: 13px; flex: none; }
  .address {
    position: absolute;
    left: 30px;
    bottom: 16px;
    font-size: 14px;
    color: var(--white);
    letter-spacing: 0.2px;
  }
</style>
</head>
<body>

<section class="card card-back">
  <div class="brand"><span class="brand-dot"></span>Northwind Delivery Group</div>
  <div class="web">www.nwdg.example</div>
</section>

<section class="card card-front">
  <svg class="wave" width="560" height="320" viewBox="0 0 560 320">
    <path d="M0,200 Q250,300 560,262 L560,320 L0,320 Z" fill="var(--blue-light)"/>
    <path d="M0,218 Q250,314 560,276 L560,320 L0,320 Z" fill="var(--blue)"/>
  </svg>

  <div class="brand"><span class="brand-dot"></span>Northwind Delivery Group</div>

  <div class="divider"></div>

  <div class="contact">
    <div class="person-name">Callum Rennie</div>
    <div class="person-role">Director</div>
    <ul class="contact-list">
      <li>
        <svg viewBox="0 0 14 14"><rect x="3.5" y="1" width="7" height="12" rx="1.2" fill="none" stroke="var(--blue-light)" stroke-width="1.3"/></svg>
        +44 1224 555 018
      </li>
      <li>
        <svg viewBox="0 0 14 14"><path d="M3 1.5 L5.2 1.5 L6 4.5 L4.6 5.6 Q5.8 8.3 8.4 9.4 L9.5 8 L12.5 8.8 L12.5 11 Q12 12.8 10 12.5 Q2.5 11 1.5 4 Q1.4 2 3 1.5 Z" fill="var(--blue-light)"/></svg>
        +44 1224 555 018
      </li>
      <li>
        <svg viewBox="0 0 14 14"><rect x="1" y="3" width="12" height="8.5" fill="none" stroke="var(--blue-light)" stroke-width="1.3"/><path d="M1 3 L7 8 L13 3" fill="none" stroke="var(--blue-light)" stroke-width="1.3"/></svg>
        callum@nwdg.example
      </li>
      <li>
        <svg viewBox="0 0 14 14"><circle cx="7" cy="7" r="5.6" fill="none" stroke="var(--blue-light)" stroke-width="1.2"/><ellipse cx="7" cy="7" rx="2.4" ry="5.6" fill="none" stroke="var(--blue-light)" stroke-width="1"/><path d="M1.4 7 H12.6" stroke="var(--blue-light)" stroke-width="1"/></svg>
        www.nwdg.example
      </li>
    </ul>
  </div>

  <div class="address">Harbour House, 12 Quay Road, Aberdeen, AB10 1XY</div>
</section>

</body>
</html>
```